A property investment company, looking to provide lovely sustainable homes for familys and individua

For a small investment business i am starting which will buy and refurbish unloved houses and apartments to rent out or resell. the company name is my family surname (HARGREAVE). <br/>i would like the design to be simple with maybe some emphasis on an ethical and sustainable/environmentally friendly approach with a branding of maybe trees blended with some houses and or apartments.<br/>The colours i like for this design would be mainly green on either a white or black background.
Target Market(s)
This business card is to be used for professional people such as estate agents
mortgage brokers, solicitors and trades people.
Industry/Entity Type
Real Estate
Contact Information for Business Card
owner/director-Martin hargreave
e-mail-martin@hvholdings.co.uk
website-hargreavehomeholdings.co.uk
mobile-07700945318
landline-02079460581
Look and feel

```html
<!DOCTYPE html>
<html lang="en">
<head>
<meta charset="utf-8">
<title>Hargreave – Business Card</title>
<link rel="stylesheet" href="https://fonts.googleapis.com/css2?family=Noto+Serif:ital,wght@0,400;0,700;1,400;1,700&display=swap">
<style>
  :root {
    --page-bg: #2a2a2b;
    --card-dark: #3b3b3d;
    --card-light: #ffffff;
    --teal: #2fb9a4;
    --lime: #9dcf3c;
    --ink: #1c1c1c;
  }
  * { margin: 0; padding: 0; box-sizing: border-box; }
  html, body { width: 1200px; height: 770px; overflow: hidden; }
  body {
    background: var(--page-bg);
    font-family: "Noto Serif", Georgia, serif;
    position: relative;
  }
  .card {
    position: absolute;
    width: 540px;
    height: 309px;
    border-radius: 16px;
    top: 230px;
    overflow: hidden;
  }
  .card--front { left: 40px; background: var(--card-dark); }
  .card--back { left: 620px; background: var(--card-light); }

  .brand-name {
    font-family: "Noto Serif", Georgia, serif;
    font-weight: 400;
    color: var(--lime);
    letter-spacing: 1px;
  }
  .card--front .brand {
    position: absolute;
    inset: 0;
    display: flex;
    align-items: center;
    justify-content: center;
    gap: 16px;
  }
  .card--front .brand-name { font-size: 54px; }
  .brand-dot {
    width: 22px; height: 22px; border-radius: 50%;
    background: var(--teal);
  }

  .card--back .brand {
    position: absolute;
    left: 34px; top: 72px;
    display: flex; align-items: center; gap: 10px;
  }
  .card--back .brand-name { font-size: 36px; }
  .card--back .brand-dot { width: 14px; height: 14px; }

  .divider {
    position: absolute;
    left: 0; top: 138px;
    width: 370px; height: 2px;
    background: var(--teal);
  }
  .person {
    position: absolute;
    right: 26px; top: 94px;
    text-align: right;
  }
  .person__name {
    font-weight: 700;
    font-size: 22px;
    color: var(--teal);
    letter-spacing: 0.5px;
  }
  .person__role {
    font-size: 15px;
    color: var(--lime);
    letter-spacing: 1px;
  }

  .contacts {
    position: absolute;
    left: 36px; top: 156px;
    list-style: none;
  }
  .contacts li {
    display: flex; align-items: center; gap: 10px;
    height: 30px;
    font-style: italic;
    font-weight: 700;
    font-size: 16px;
    color: var(--ink);
    letter-spacing: 0.8px;
  }
  .contacts svg { width: 22px; height: 22px; flex: none; }
</style>
</head>
<body>

<section class="card card--front">
  <div class="brand">
    <span class="brand-dot"></span>
    <span class="brand-name">Hargreave</span>
  </div>
</section>

<section class="card card--back">
  <div class="brand">
    <span class="brand-dot"></span>
    <span class="brand-name">Hargreave</span>
  </div>
  <div class="divider"></div>

  <div class="person">
    <div class="person__name">Martin hargreave</div>
    <div class="person__role">owner/director</div>
  </div>

  <ul class="contacts">
    <li>
      <svg viewBox="0 0 22 22" aria-hidden="true"><circle cx="11" cy="11" r="11" fill="var(--lime)"/><rect x="7.5" y="4.5" width="7" height="13" rx="1.5" fill="none" stroke="#fff" stroke-width="1.5"/><circle cx="11" cy="15.2" r="0.9" fill="#fff"/></svg>
      07700945318
    </li>
    <li>
      <svg viewBox="0 0 22 22" aria-hidden="true"><circle cx="11" cy="11" r="11" fill="var(--lime)"/><path d="M5 9.5c0-2 12-2 12 0v1.3h-3V9.6h-6v1.2H5z" fill="#fff"/><path d="M7 12h8l1 4H6z" fill="#fff"/><circle cx="11" cy="13.8" r="1.2" fill="var(--lime)"/></svg>
      02079460581
    </li>
    <li>
      <svg viewBox="0 0 22 22" aria-hidden="true"><circle cx="11" cy="11" r="11" fill="var(--lime)"/><rect x="5" y="7" width="12" height="8.5" rx="1" fill="#fff"/><path d="M5.5 7.5 11 12l5.5-4.5" fill="none" stroke="var(--lime)" stroke-width="1.2"/></svg>
      martin@hvholdings.co.uk
    </li>
    <li>
      <svg viewBox="0 0 22 22" aria-hidden="true"><circle cx="11" cy="11" r="11" fill="var(--lime)"/><g fill="none" stroke="#fff" stroke-width="1.2"><circle cx="11" cy="11" r="6"/><ellipse cx="11" cy="11" rx="2.6" ry="6"/><path d="M5 11h12M6 8h10M6 14h10"/></g></svg>
      hargreavehomeholdings.co.uk
    </li>
  </ul>
</section>

</body>
</html>
```